The Maplewick Academy Web Page

We need a web design for our Day Care Center based in Brandon, Florida. We are targeting child care and educational services to middle class parents, specially the mother. We would like to see designs that matches attached logo mark. The final design should communicate higher standards for day care and educational services.

Target Market(s)

Middle class parents in the State of Florida

Coding

Number of Pages Required

5+ page

```html
<!DOCTYPE html>
<html lang="en">
<head>
<meta charset="utf-8">
<title>The Maplewick Academy</title>
<link href="https://fonts.googleapis.com/css2?family=Open+Sans:wght@400;600;700&display=swap" rel="stylesheet">
<style>
:root{
  --navy:#0c2444;
  --navy-deep:#0a1f3c;
  --cream:#fdf8dc;
  --cream-light:#fffcea;
  --gold:#f5b51c;
  --gold-light:#ffd23e;
  --orange:#d9782a;
  --ink:#1d2b45;
  --white:#ffffff;
  --card-border:#e3e0cf;
}
*{box-sizing:border-box;margin:0;padding:0}
html,body{width:743px;height:1200px;overflow:hidden}
body{font-family:'Open Sans',sans-serif;color:var(--ink);background:var(--white);position:relative}

.site-header{position:absolute;left:0;top:0;width:743px;height:145px;background:var(--white)}
.brand{position:absolute;left:0;right:0;top:48px;display:flex;align-items:center;justify-content:center;gap:10px}
.brand-dot{width:22px;height:22px;border-radius:50%;background:var(--navy)}
.brand-name{font-size:20px;font-weight:700;color:var(--navy);letter-spacing:.3px}
.header-toggle{position:absolute;left:667px;top:0;width:21px;height:21px;background:var(--navy);border-radius:0 0 10px 10px;display:flex;align-items:center;justify-content:center}

.main-nav{position:absolute;left:0;top:145px;width:743px;height:40px;border-top:2px solid var(--navy);border-bottom:1px solid var(--navy);background:linear-gradient(var(--cream-light),var(--cream));display:flex;align-items:center;padding-left:70px}
.nav-item{font-size:10px;color:var(--ink);padding:4px 7px;border-radius:12px;display:flex;align-items:center;gap:2px;margin-right:5px}
.nav-item .caret{font-size:7px}
.nav-item.is-active{background:var(--navy);color:var(--white);padding:5px 8px}

.hero{position:absolute;left:0;top:185px;width:743px;height:418px;background:
 radial-gradient(ellipse at 48% 45%,#c24a52 0%,#b13b46 18%,rgba(177,59,70,0) 40%),
 radial-gradient(ellipse at 15% 60%,#e7c8b0 0%,rgba(231,200,176,0) 35%),
 linear-gradient(90deg,#d9a98a 0%,#e8d88a 40%,#e6df9a 70%,#c9c89c 100%)}
.hero-copy{position:absolute;left:197px;top:241px;width:349px;text-align:center;color:var(--white)}
.hero-rule{height:1px;background:var(--white);position:relative}
.hero-rule span{position:absolute;left:50%;top:-4px;transform:translateX(-50%);font-size:8px;line-height:8px}
.hero-tagline{font-size:13px;line-height:17px;padding:8px 0 10px}
.hero-title{font-size:23px;font-weight:700;letter-spacing:.4px;margin-top:14px}
.hero-button{display:inline-block;margin-top:14px;width:71px;height:20px;border-radius:10px;background:var(--gold);color:var(--white);font-size:8px;line-height:20px}
.hero-notch{position:absolute;left:322px;top:584px;width:98px;height:40px;border-radius:49px 49px 0 0;background:var(--navy)}
.hero-dots{position:absolute;left:356px;top:594px;display:flex;gap:3px}
.hero-dots i{width:8px;height:8px;border-radius:50%;background:var(--white)}
.hero-dots i.alt{background:var(--gold);border:1px solid var(--white)}

.welcome{position:absolute;left:0;top:603px;width:743px;height:203px;background:var(--navy);color:var(--white);text-align:center}
.welcome h1{font-size:18px;font-weight:700;margin-top:65px;letter-spacing:.3px}
.welcome p{font-size:9.5px;line-height:11.5px;width:510px;margin:11px auto 0}
.welcome .learn{display:block;font-size:9.5px;margin-top:19px}

.features{position:absolute;left:0;top:806px;width:743px;height:352px;background:var(--cream)}
.card{position:absolute;background:var(--white);border:1px solid var(--card-border);box-shadow:0 0 0 2px #f4f0da}
.card h2{font-size:14.5px;font-weight:400;color:var(--ink);position:absolute;left:11px;top:14px}
.card-photo{position:absolute;left:12px;top:38px;width:72px;height:70px}
.photo-a{background:linear-gradient(135deg,#f1efe8,#d8c8b4 50%,#9dbf6e)}
.photo-b{background:linear-gradient(135deg,#3b3a3e,#c98f80 50%,#e07c9b)}
.card-text{position:absolute;left:96px;top:38px;width:98px;font-size:7.5px;line-height:9px;color:var(--ink)}
.card-link{position:absolute;left:96px;top:95px;font-size:7.5px;color:var(--orange)}

.admissions h2{left:15px;top:18px;display:flex;align-items:center;gap:6px}
.admissions .adm-photo{position:absolute;left:14px;top:45px;width:133px;height:80px;background:linear-gradient(90deg,#5b4c42,#c4a387 45%,#d88b52)}
.admissions .adm-text{position:absolute;left:15px;top:141px;width:135px;font-size:7.5px;line-height:9px}
.adm-links{position:absolute;left:14px;top:180px;list-style:none}
.adm-links li{font-size:8.5px;display:flex;align-items:center;gap:4px;margin-bottom:7px}

.site-footer{position:absolute;left:0;top:1158px;width:743px;height:42px;background:var(--navy);color:var(--white)}
.footer-links{position:absolute;left:72px;top:15px;font-size:7.5px}
.social{position:absolute;left:529px;top:14px;display:flex;gap:10px;align-items:center}
.social .round{width:11px;height:11px;border-radius:50%;background:#8a9ab3}
.copyright{position:absolute;left:630px;top:15px;font-size:9px}
</style>
</head>
<body>
<header class="site-header">
  <div class="brand"><span class="brand-dot"></span><span class="brand-name">The Maplewick Academy</span></div>
  <div class="header-toggle"><svg width="9" height="6" viewBox="0 0 9 6"><path d="M1 1l3.5 3.5L8 1" fill="none" stroke="#fff" stroke-width="1.3"/></svg></div>
</header>

<nav class="main-nav">
  <span class="nav-item">Home</span>
  <span class="nav-item is-active">Admissions<span class="caret">&#8964;</span></span>
  <span class="nav-item">Philosophy<span class="caret">&#8964;</span></span>
  <span class="nav-item">Programs<span class="caret">&#8964;</span></span>
  <span class="nav-item">Services<span class="caret">&#8964;</span></span>
  <span class="nav-item">Campuses<span class="caret">&#8964;</span></span>
  <span class="nav-item">Franchises<span class="caret">&#8964;</span></span>
  <span class="nav-item">Business<span class="caret">&#8964;</span></span>
  <span class="nav-item">Contact</span>
  <span class="nav-item">More<span class="caret">&#8964;</span></span>
</nav>

<section class="hero" role="img" aria-label="Photo of a smiling teacher clapping with two young children in a bright classroom"></section>
<div class="hero-copy">
  <div class="hero-rule"><span>&#9733;</span></div>
  <p class="hero-tagline">We deliver child care and educational services<br>to middle class parents</p>
  <div class="hero-rule"><span>&#9733;</span></div>
  <p class="hero-title">HOME SCHOOL SUPPORT</p>
  <span class="hero-button">CLICK HERE</span>
</div>
<div class="hero-notch"></div>
<div class="hero-dots"><i></i><i class="alt"></i><i class="alt"></i></div>

<section class="welcome">
  <h1>WELCOME TO THE MAPLEWICK ACADEMY</h1>
  <p>Lorem ipsum dolor sit amet, consectetur adipisicing elit, sed incididunt ut labore et dolore magna aliqua. Ut enim ad veniam, quis ullamco laboris nisi aliquip commodo consequat. Duis aute irure dolor in in voluptate velit esse cillum dolore eu fugiat nulla pariatur. Excepteur sint occaecat cupidatat</p>
  <span class="learn">Learn More&gt;&gt;</span>
</section>

<section class="features">
  <article class="card" style="left:74px;top:48px;width:201px;height:125px">
    <h2>Philosophy</h2>
    <div class="card-photo photo-a" role="img" aria-label="Photo of a mother and baby with a plant"></div>
    <p class="card-text">Lorem ipsum dolor sit amet, adipisicing elit, sed eiusmod incididunt ut labore et aliqua. Ut enim ad minim veniam</p>
    <span class="card-link">Learn More&gt;&gt;</span>
  </article>
  <article class="card" style="left:288px;top:48px;width:201px;height:125px">
    <h2>Franchises</h2>
    <div class="card-photo photo-b" role="img" aria-label="Photo of a mother reading with a baby"></div>
    <p class="card-text">Lorem ipsum dolor sit amet, adipisicing elit, sed eiusmod incididunt ut labore et aliqua. Ut enim ad minim veniam</p>
    <span class="card-link">Learn More&gt;&gt;</span>
  </article>
  <article class="card" style="left:74px;top:186px;width:201px;height:125px">
    <h2>Programs</h2>
    <div class="card-photo photo-a" role="img" aria-label="Photo of a mother and baby with a plant"></div>
    <p class="card-text">Lorem ipsum dolor sit amet, adipisicing elit, sed eiusmod incididunt ut labore et aliqua. Ut enim ad minim veniam</p>
    <span class="card-link">Learn More&gt;&gt;</span>
  </article>
  <article class="card" style="left:288px;top:186px;width:201px;height:125px">
    <h2>Campuses</h2>
    <div class="card-photo photo-b" role="img" aria-label="Photo of a mother reading with a baby"></div>
    <p class="card-text">Lorem ipsum dolor sit amet, adipisicing elit, sed eiusmod incididunt ut labore et aliqua. Ut enim ad minim veniam</p>
    <span class="card-link">Learn More&gt;&gt;</span>
  </article>
  <article class="card admissions" style="left:503px;top:49px;width:160px;height:260px">
    <h2><svg width="12" height="12" viewBox="0 0 24 24"><path d="M12 1l3.4 7 7.6 1-5.5 5.3 1.3 7.7L12 18.4 5.2 22l1.3-7.7L1 9l7.6-1z" fill="#0c2444"/></svg>Admissions</h2>
    <div class="adm-photo" role="img" aria-label="Photo of two babies playing with toys on a nursery floor"></div>
    <p class="adm-text">Lorem ipsum dolor sit adipisicing elit, sed incididunt ut labore et aliqua. Ut enim ad minim veniam</p>
    <ul class="adm-links">
      <li><svg width="9" height="9" viewBox="0 0 24 24"><path d="M12 1l3.4 7 7.6 1-5.5 5.3 1.3 7.7L12 18.4 5.2 22l1.3-7.7L1 9l7.6-1z" fill="#0c2444"/></svg>Apply for Admission</li>
      <li><svg width="9" height="9" viewBox="0 0 24 24"><path d="M12 1l3.4 7 7.6 1-5.5 5.3 1.3 7.7L12 18.4 5.2 22l1.3-7.7L1 9l7.6-1z" fill="#0c2444"/></svg>Schedule a Campus Tour</li>
      <li><svg width="9" height="9" viewBox="0 0 24 24"><path d="M12 1l3.4 7 7.6 1-5.5 5.3 1.3 7.7L12 18.4 5.2 22l1.3-7.7L1 9l7.6-1z" fill="#0c2444"/></svg>Enrollment Policy</li>
    </ul>
  </article>
</section>

<footer class="site-footer">
  <p class="footer-links">Home &nbsp;/&nbsp; Admissions &nbsp;/&nbsp; Philosophy &nbsp;/&nbsp; Programs &nbsp;/&nbsp; Services &nbsp;/&nbsp; Campuses &nbsp;/&nbsp; Franchises &nbsp;/&nbsp; Business &nbsp;/&nbsp; Contact &nbsp;/&nbsp; More</p>
  <div class="social">
    <span class="round"></span>
    <span class="round"></span>
    <svg width="13" height="10" viewBox="0 0 13 10"><rect x="0.5" y="0.5" width="12" height="9" fill="#8a9ab3"/><path d="M0.5 0.5l6 5 6-5" fill="none" stroke="#0c2444" stroke-width="1"/></svg>
  </div>
  <p class="copyright">&copy; 2015</p>
</footer>
</body>
</html>
```